Kanomiva business cards/stationary
Relocation Support Services
I need single sided standard sized Business Card [3.5" x 2"]
Designer's discretion
Professional
Ned Palmer
President
5-31-08 Nishimorino
Suginami-ku, Tokyo 168-0072
ned@kanomiva.com
www.kanomiva.com
Have not yet received logo files from designer. I will be using
Will upload Al format as soon as I receive from designer.
Kanomiva logo to be used

```html
<!DOCTYPE html>
<html lang="en">
<head>
<meta charset="utf-8">
<title>Kanomiva Business Card</title>
<link href="https://fonts.googleapis.com/css2?family=Source+Sans+3:wght@400;600;700&display=swap" rel="stylesheet">
<style>
  :root {
    --page-bg: #e9e6e2;
    --card-white: #ffffff;
    --brand-red: #c8102e;
    --brand-red-light: #e0283f;
    --brand-red-dark: #8e0a1c;
    --ink-dark: #3a3a3c;
    --text-light: #ffffff;
    --divider-grey: #9a9a9a;
  }
  html, body {
    margin: 0;
    padding: 0;
    width: 1200px;
    height: 780px;
    overflow: hidden;
    background: var(--page-bg);
    font-family: "Source Sans 3", "Helvetica Neue", Arial, sans-serif;
  }
  .business-card {
    position: absolute;
    left: 75px;
    top: 90px;
    width: 1050px;
    height: 600px;
    border-radius: 30px;
    overflow: hidden;
    box-shadow: 0 10px 30px rgba(0,0,0,0.25);
    background: var(--card-white);
  }
  .card-art {
    position: absolute;
    inset: 0;
  }
  .brand-lockup {
    position: absolute;
    left: 70px;
    top: 270px;
    display: flex;
    align-items: center;
    gap: 16px;
  }
  .brand-mark {
    width: 34px;
    height: 34px;
    border-radius: 50%;
    background: var(--brand-red);
  }
  .brand-name {
    font-size: 64px;
    font-weight: 700;
    color: var(--ink-dark);
    letter-spacing: -1px;
    line-height: 1;
  }
  .holder {
    position: absolute;
    right: 50px;
    top: 30px;
    text-align: right;
    color: var(--text-light);
  }
  .holder-name {
    font-size: 36px;
    font-weight: 700;
    line-height: 1.1;
  }
  .holder-title {
    font-size: 27px;
    font-weight: 400;
    line-height: 1.2;
  }
  .contact-list {
    position: absolute;
    right: 40px;
    bottom: 40px;
    margin: 0;
    padding: 0;
    list-style: none;
    color: var(--text-light);
    font-size: 25px;
    line-height: 38px;
  }
  .contact-item {
    display: flex;
    justify-content: flex-end;
    align-items: center;
    gap: 12px;
  }
  .contact-icon {
    width: 24px;
    height: 24px;
    flex: none;
  }
  .contact-icon.blank { visibility: hidden; }
</style>
</head>
<body>
  <div class="business-card">
    <svg class="card-art" width="1050" height="600" viewBox="0 0 1050 600" aria-hidden="true">
      <defs>
        <radialGradient id="redPanel" cx="0.45" cy="0.45" r="0.7">
          <stop offset="0" stop-color="var(--brand-red-light)"/>
          <stop offset="0.6" stop-color="var(--brand-red)"/>
          <stop offset="1" stop-color="var(--brand-red-dark)"/>
        </radialGradient>
        <linearGradient id="divider" x1="0" y1="0" x2="1" y2="0">
          <stop offset="0" stop-color="#ffffff" stop-opacity="0"/>
          <stop offset="1" stop-color="var(--divider-grey)"/>
        </linearGradient>
      </defs>
      <path d="M 430 0 C 505 190, 490 420, 375 600 L 395 600 C 510 420, 525 190, 452 0 Z" fill="url(#divider)"/>
      <path d="M 452 0 C 525 190, 510 420, 395 600 L 1050 600 L 1050 0 Z" fill="url(#redPanel)"/>
    </svg>

    <div class="brand-lockup">
      <span class="brand-mark"></span>
      <span class="brand-name">Kanomiva</span>
    </div>

    <div class="holder">
      <div class="holder-name">Ned Palmer</div>
      <div class="holder-title">President</div>
    </div>

    <ul class="contact-list">
      <li class="contact-item"><span>5-31-08 Nishimorino</span><svg class="contact-icon blank" viewBox="0 0 24 24"></svg></li>
      <li class="contact-item"><span>Suginami-ku, Tokyo 168-0072</span><svg class="contact-icon blank" viewBox="0 0 24 24"></svg></li>
      <li class="contact-item"><span>+81 (0)80-4192-3358</span>
        <svg class="contact-icon" viewBox="0 0 24 24" aria-label="Phone"><path fill="#fff" d="M6.6 10.8c1.4 2.8 3.8 5.1 6.6 6.6l2.2-2.2c.3-.3.7-.4 1-.2 1.1.4 2.3.6 3.6.6.6 0 1 .4 1 1V20c0 .6-.4 1-1 1C10.6 21 3 13.4 3 4c0-.6.4-1 1-1h3.5c.6 0 1 .4 1 1 0 1.3.2 2.5.6 3.6.1.3 0 .7-.2 1z"/></svg></li>
      <li class="contact-item"><span>ned@kanomiva.com</span>
        <svg class="contact-icon" viewBox="0 0 24 24" aria-label="Email"><text x="12" y="19" text-anchor="middle" font-size="22" font-weight="700" fill="#fff" font-family="Arial, sans-serif">@</text></svg></li>
      <li class="contact-item"><span>www.kanomiva.com</span>
        <svg class="contact-icon" viewBox="0 0 24 24" aria-label="Website"><g fill="none" stroke="#fff" stroke-width="2"><circle cx="12" cy="12" r="9"/><ellipse cx="12" cy="12" rx="4" ry="9"/><line x1="3" y1="12" x2="21" y2="12"/></g></svg></li>
    </ul>
  </div>
</body>
</html>
```